The Wardrobe Sage needs a business card

The wardrobe sage is a lead generation service serving the Custom Closet industry.

Here is the basic card information:

The Wardrobe Sage
Dorian Pettigrew
Owner/CEO
Greenvale, NC
704-318-5527 Cell
Email: dpettigrew@TheWardrobeSage.com

Additional information for the card:

"High quality, flat rate lead generation exclusively for the custom closet industry"

Bullet points for the back:

- Low fixed cost
- Easy to budget
- Guaranteed qualified Leeds
- Exclusivity per city

Logo attached, head shot attached. Photos of closet systems attached

```html
<!DOCTYPE html>
<html lang="en">
<head>
<meta charset="utf-8">
<title>The Wardrobe Sage — Business Card</title>
<link href="https://fonts.googleapis.com/css2?family=Crimson+Pro:ital,wght@0,400;0,600;1,600&family=Lato:wght@300;400&display=swap" rel="stylesheet">
<style>
  :root {
    --bg: #2b2d30;
    --copper: #a3652e;
    --slate: #545456;
    --paper: #ffffff;
    --ink: #3a3a3c;
    --rule: #6b6b6d;
    --muted: #7a7a7c;
  }
  * { margin: 0; padding: 0; box-sizing: border-box; }
  html, body { width: 1200px; height: 952px; overflow: hidden; background: var(--bg); }
  .canvas { position: relative; width: 1200px; height: 952px; }

  .card {
    position: absolute;
    width: 560px;
    height: 320px;
    border-radius: 22px;
    overflow: hidden;
    box-shadow: 0 14px 30px rgba(0,0,0,.45);
  }

  /* Back of card */
  .card-back { left: 80px; top: 540px; background: var(--copper); }
  .card-back .band {
    position: absolute; left: 0; right: 0; bottom: 0; height: 104px;
    background: var(--slate);
    border-top: 6px solid var(--paper);
  }
  .card-back .brand-name {
    position: absolute; left: 0; right: 0; top: 74px;
    text-align: center;
    font-family: "Crimson Pro", serif; font-weight: 600;
    font-size: 52px; color: var(--paper); letter-spacing: .5px;
  }
  .benefits {
    position: absolute; left: 40px; right: 30px; top: 24px;
    display: grid; grid-template-columns: 1fr 1.5fr; row-gap: 6px; column-gap: 20px;
    list-style: none;
    font-family: "Crimson Pro", serif; font-weight: 600;
    font-size: 19px; color: var(--paper); letter-spacing: .6px;
  }
  .benefits li::before { content: "•"; margin-right: 6px; }

  /* Front of card */
  .card-front { left: 560px; top: 110px; background: var(--paper); }
  .card-front .top-rule {
    position: absolute; left: 0; right: 0; top: 40px; height: 1px; background: var(--rule);
  }
  .tagline {
    position: absolute; right: 34px; top: 56px; width: 360px;
    text-align: center;
    font-family: "Crimson Pro", serif; font-style: italic; font-weight: 600;
    font-size: 19px; line-height: 1.2; color: var(--copper);
  }
  .card-front .brand-name {
    position: absolute; right: 60px; top: 130px;
    font-family: "Crimson Pro", serif; font-weight: 600;
    font-size: 34px; color: var(--copper);
  }
  .person { position: absolute; left: 40px; top: 196px; }
  .person .name {
    font-family: "Crimson Pro", serif; font-weight: 600;
    font-size: 17px; letter-spacing: 1.2px; text-transform: uppercase; color: var(--ink);
  }
  .person .role {
    font-family: "Lato", sans-serif; font-weight: 300;
    font-size: 12px; color: var(--muted); margin-top: 2px;
  }
  .contacts {
    position: absolute; left: 226px; top: 200px;
    list-style: none;
    font-family: "Lato", sans-serif; font-weight: 300;
    font-size: 13px; color: var(--ink);
  }
  .contacts li { display: flex; align-items: center; gap: 8px; margin-bottom: 7px; }
  .contacts svg { width: 16px; height: 16px; flex: none; }
</style>
</head>
<body>
<main class="canvas">

  <section class="card card-front" aria-label="Card front">
    <div class="top-rule"></div>
    <p class="tagline">"High quality, flat rate lead generation exclusively for the custom closet industry"</p>
    <div class="brand-name">The Wardrobe Sage</div>
    <div class="person">
      <div class="name">Dorian Pettigrew</div>
      <div class="role">Owner/CEO</div>
    </div>
    <ul class="contacts">
      <li>
        <svg viewBox="0 0 16 16"><rect width="16" height="16" rx="2" fill="#a3652e"/><path d="M8 3.2a3 3 0 0 0-3 3c0 2.3 3 6 3 6s3-3.7 3-6a3 3 0 0 0-3-3zm0 4.2a1.2 1.2 0 1 1 0-2.4 1.2 1.2 0 0 1 0 2.4z" fill="#fff"/></svg>
        Greenvale, NC
      </li>
      <li>
        <svg viewBox="0 0 16 16"><rect width="16" height="16" rx="2" fill="#a3652e"/><path d="M5 3.5l1.8 2.2-1 1.2a6 6 0 0 0 3.3 3.3l1.2-1 2.2 1.8-1 1.5c-4 0-7.5-3.5-7.5-7.5z" fill="#fff"/></svg>
        704-318-5527
      </li>
      <li>
        <svg viewBox="0 0 16 16"><rect width="16" height="16" rx="2" fill="#a3652e"/><rect x="3.5" y="5" width="9" height="6.5" fill="none" stroke="#fff" stroke-width="1.2"/><path d="M3.5 5l4.5 3.6L12.5 5" fill="none" stroke="#fff" stroke-width="1.2"/></svg>
        dpettigrew@TheWardrobeSage.com
      </li>
    </ul>
  </section>

  <section class="card card-back" aria-label="Card back">
    <div class="brand-name">The Wardrobe Sage</div>
    <div class="band">
      <ul class="benefits">
        <li>Low Fixed Cost</li>
        <li>Guaranteed Qualified Leeds</li>
        <li>Easy To Budget</li>
        <li>Exclusivity Per City</li>
      </ul>
    </div>
  </section>

</main>
</body>
</html>
```